Vesit cards for web development company

We need a business card design for our company. The company develops online platforms and conducts marketing consulting. Company logo. The cards must fit in with us (a junior start UP), but they must also be professional enough to impress with investors like banks. We wish you a combination of classic and modern design

Target Market(s)

Business partners and IT and marketing customers

Industry/Entity Type

It Company

Contact Information for Business Card

Folgende Information müssen Drauf.
Name, Position, Telefon Nr., Mobile Nr., E-Mail adresse, Optional sind noch Webadresse und HRB Nummer

Colors

Designer to choose colors to be used in the design.

Requirements
Must have
• The cards have to fit into the logo later and have to be dynamic and serious at the same time

```html
<!DOCTYPE html>
<html lang="en">
<head>
<meta charset="utf-8">
<title>Kestrel Development – Business Cards</title>
<link rel="stylesheet" href="https://fonts.googleapis.com/css2?family=Exo+2:wght@400;500;700&display=swap">
<style>
  :root {
    --brand-blue: #1173bb;
    --ink: #3a3a3a;
    --muted: #8a8c8f;
    --paper: #ffffff;
    --backdrop: #e9e7e4;
  }
  * { margin: 0; padding: 0; box-sizing: border-box; }
  html, body {
    width: 1200px; height: 1200px; overflow: hidden;
    background: var(--backdrop);
    font-family: "Exo 2", sans-serif;
  }
  .sheet {
    width: 1200px; height: 1200px;
    display: flex; flex-direction: column; align-items: center; justify-content: center;
    gap: 80px;
  }
  .card {
    width: 840px; height: 480px;
    box-shadow: 0 6px 24px rgba(0,0,0,0.18);
    position: relative;
  }
  .card--front {
    background: var(--brand-blue);
    display: flex; align-items: center; justify-content: center;
  }
  .wordmark {
    display: flex; align-items: center; gap: 18px;
    font-weight: 700; letter-spacing: 2px; text-transform: uppercase;
  }
  .wordmark__dot {
    width: 30px; height: 30px; border-radius: 50%;
  }
  .card--front .wordmark { color: var(--paper); font-size: 46px; }
  .card--front .wordmark__dot { background: var(--paper); }

  .card--back {
    background: var(--paper);
    display: flex; align-items: center;
    padding: 0 60px 0 70px;
  }
  .identity { width: 380px; }
  .card--back .wordmark { color: var(--brand-blue); font-size: 34px; }
  .card--back .wordmark__dot { background: var(--brand-blue); width: 24px; height: 24px; }
  .registry {
    margin-top: 10px; margin-left: 42px;
    color: var(--muted); font-size: 22px; font-weight: 400; letter-spacing: 1px;
  }
  .divider {
    width: 2px; height: 210px; background: var(--brand-blue);
    margin: 0 34px 0 10px;
  }
  .contact { color: var(--ink); }
  .contact__name {
    color: var(--brand-blue); font-size: 34px; font-weight: 700; letter-spacing: 0.5px;
  }
  .contact__role { font-size: 19px; margin-bottom: 14px; }
  .contact__list { list-style: none; font-size: 19px; }
  .contact__item { display: flex; align-items: center; gap: 10px; line-height: 30px; }
  .contact__item--gap { margin-top: 12px; }
  .icon {
    width: 20px; height: 20px; flex: none;
  }
</style>
</head>
<body>
<main class="sheet">
  <section class="card card--front" aria-label="Card front">
    <div class="wordmark"><span class="wordmark__dot"></span>Kestrel Development</div>
  </section>

  <section class="card card--back" aria-label="Card back">
    <div class="identity">
      <div class="wordmark"><span class="wordmark__dot"></span>Kestrel Development</div>
      <p class="registry">HRB No. XX-XX-XXXX</p>
    </div>
    <div class="divider"></div>
    <div class="contact">
      <h1 class="contact__name">JOHN DOE</h1>
      <p class="contact__role">Director</p>
      <ul class="contact__list">
        <li class="contact__item">
          <svg class="icon" viewBox="0 0 20 20"><circle cx="10" cy="10" r="10" fill="#1173bb"/><path d="M7 5.5l1.6 1.6-1 1.2a6 6 0 0 0 4.1 4.1l1.2-1 1.6 1.6-1.2 1.4C10 14.2 5.8 10 5.6 6.7z" fill="#fff"/></svg>
          1-234-567890
        </li>
        <li class="contact__item">
          <svg class="icon" viewBox="0 0 20 20"><circle cx="10" cy="10" r="10" fill="#1173bb"/><rect x="7" y="4.5" width="6" height="11" rx="1" fill="#fff"/><rect x="8" y="6" width="4" height="6.5" fill="#1173bb"/></svg>
          1-234-5678900
        </li>
        <li class="contact__item contact__item--gap">
          <svg class="icon" viewBox="0 0 20 20"><circle cx="10" cy="10" r="10" fill="#1173bb"/><circle cx="10" cy="10" r="5.5" fill="none" stroke="#fff" stroke-width="1.2"/><ellipse cx="10" cy="10" rx="2.4" ry="5.5" fill="none" stroke="#fff" stroke-width="1"/><line x1="4.5" y1="10" x2="15.5" y2="10" stroke="#fff" stroke-width="1"/></svg>
          www.companyname.com
        </li>
        <li class="contact__item">
          <svg class="icon" viewBox="0 0 20 20"><circle cx="10" cy="10" r="10" fill="#1173bb"/><rect x="5" y="6.5" width="10" height="7" fill="#fff"/><path d="M5 6.5l5 4 5-4" fill="none" stroke="#1173bb" stroke-width="1"/></svg>
          john@companyname.com
        </li>
      </ul>
    </div>
  </section>
</main>
</body>
</html>
```